Biz technology consulting firm like a global company (better than Corvantis, etc)

Check word document high level requirements, a_design_webpage_content attached providing more details for content and message to convey to potential customers..  Create a crisp, clear and engaging business consulting website design that allows the user to understand the value that Brimquarta can deliver to their company.  We focus on innovation, simplification, creative solutions, digital transformations ERP, CRM, Analytics, project management, making IT simple and coaching enterprises how to align and implement technologies to support business strategy and goals. Whether a startup or a global billion dollar firm, we increase EBITDA through innovation and digital transformation.  

I desire to have sections that highlight each of the core areas such as: (**Please see  brimquarta.example and the design word document that is attached below for core areas of focus**)

Feel free to go to Brimquarta.example and review the basic categories to understand at a very high level the categories that are key.

Help me create a brand and website that engages startups, Private Equity firms seeking carve-out, integration experience and large corporate enterprises searching to convert to data driven and customer focused enterprises.  
Hero section with a tagline that emphasizes the company's focus on Walking UP bolder.  We help you visualize outcomes with a positive and collaborative solution driven mindset.  When you look at life through a different "positive" lens, you can convert all problems to opportunities.  Align your IT team with your business goals and you quickly realize the value of all processes and technology deployed in your enterprise; increasing EBITDA, morale, and long term success.

We evaluate your current state, create a custom roadmap for alignment, coach  and empower you to lead while removing the uncertainty and silos.  Partner with the experts who help make business and technology simple and effective
Call-to-action section encouraging visitors to learn more about the company's services and expertise
Services -- detail provided in the attached word document (please use)
Section providing an overview of the company's services, including digital transformation, strategy, change management, CRM, ERP, automation, AI, data / analytics, process optimization, carve-outs, integrations, scaling, risk mitigation, security and marketing.
Call-to-action section encouraging visitors to learn more about the company's expertise and how it can help their business and encouraging visitors to schedule a consultation or assessment.
Footer
Navigation menu
Contact information
LinkedIn link
The website should have a modern and professional design, with a focus on clear messaging and easy navigation. The color scheme will be clean and simple, with a mix of colors to convey trust, reliability, and innovation. The website will be optimized for search engines and mobile devices, ensuring that visitors can easily access the site from any device.

Target Market(s)

Companies who desire to grow their business, optimize their processes, maximize the output of human capital and profitablity.

Industry/Entity Type

Business Technology consulting

Coding

Coded - Design and coding required

Number of Pages Required

4 page

Font styles to use
Other font styles liked:
• designer should choose for professional audience

Requirements
Must have
• easy navigation, engaging flow, professional layout and colors that represent confidence, excellence and innovation in a world full of change.
Nice to have
• I would like to see you blend in the play on DELTA's (changes that we face in business and life), the different way we may look at things and the unique way we solve problems. All of these are options to Walk UP bolder and leverage the unique views of individuals, millions of data points, workflow and technology enablers to deliver maximize value to your enterprise

```html
<!DOCTYPE html>
<html lang="en">
<head>
<meta charset="utf-8">
<title>Brimquarta — Business Technology Consulting</title>
<link href="https://fonts.googleapis.com/css2?family=Poppins:wght@300;400;500;600;700&display=swap" rel="stylesheet">
<style>
  :root{
    --brand-blue:#1769b8;
    --ink:#111318;
    --body:#4a4d55;
    --accent:#f0471c;
    --tint:#f3f4fb;
    --tri:#eef0f8;
    --navy-1:#0c2a45;
    --navy-2:#1d4466;
    --white:#ffffff;
  }
  *{box-sizing:border-box;margin:0;padding:0}
  html,body{width:1200px;height:1200px;overflow:hidden;background:var(--white)}
  body{font-family:'Poppins',sans-serif;color:var(--ink);position:relative}
  .abs{position:absolute}

  /* header */
  .brand{left:453px;top:9px;display:flex;align-items:center;gap:4px;font-weight:500;font-size:8px;color:var(--ink)}
  .brand-dot{width:10px;height:10px;background:var(--brand-blue)}
  .nav{left:552px;top:13px;display:flex;gap:9px;font-size:3.8px;font-weight:500;letter-spacing:.1px}
  .nav a{color:var(--ink);text-decoration:none}
  .nav a.active{color:var(--brand-blue)}
  .search{left:673px;top:12px}
  .call-btn{left:703px;top:9px;width:61px;height:15px;background:var(--brand-blue);color:var(--white);font-size:4px;display:flex;align-items:center;justify-content:center;gap:4px}

  /* hero */
  .hero-photo{left:410px;top:30px;width:396px;height:212px;background:linear-gradient(100deg,var(--navy-1) 0%,var(--navy-2) 55%,#2e5a7e 75%,var(--navy-1) 100%)}
  .hero-kicker{left:459px;top:97px;font-size:4.3px;font-weight:700;color:var(--white)}
  .hero-title{left:458px;top:104px;font-size:17px;line-height:20px;font-weight:500;color:var(--white)}
  .hero-title b{font-weight:700}
  .hero-copy{left:458px;top:151px;width:110px;font-size:4.3px;line-height:7.7px;color:var(--white)}
  .hero-btn{left:458px;top:194px;width:52px;height:18px;border:1px solid var(--white);background:var(--brand-blue);color:var(--white);font-size:5.3px;display:flex;align-items:center;justify-content:center;text-decoration:underline;border-radius:1px}

  /* about */
  .kicker{font-size:5.3px;color:var(--accent);font-weight:500}
  .about-kicker{left:457px;top:270px}
  .about-title{left:457px;top:280px;width:115px;font-size:11px;line-height:13.3px;font-weight:700}
  .about-copy{left:457px;top:340px;width:112px;font-size:4.3px;line-height:7.8px;color:var(--body)}
  .about-btn{left:457px;top:412px;width:61px;height:13px;background:var(--brand-blue);color:var(--white);font-size:4.4px;font-weight:500;display:flex;align-items:center;justify-content:center}
  .photo-back{left:654px;top:265px;width:119px;height:79px;background:linear-gradient(120deg,#1a2d3f,#3a4d5e 40%,#b0855a 70%,#2a2420)}
  .photo-front{left:593px;top:281px;width:86px;height:75px;background:linear-gradient(140deg,#c9d3dd,#6e89a6 50%,#1c3e6c);border:1px solid var(--white)}

  .tri{position:absolute;top:0;left:0}

  /* focus */
  .focus-kicker{left:0;width:1238px;top:494px;text-align:center;font-weight:600}
  .focus-title{left:0;width:1238px;top:501px;text-align:center;font-size:11px;font-weight:500}
  .focus-sub{left:0;width:1238px;top:523px;text-align:center;font-size:4.4px;color:var(--body)}

  .grid{left:452px;top:566px;width:312px;display:grid;grid-template-columns:repeat(3,104px);grid-template-rows:repeat(3,89px)}
  .cell{display:flex;flex-direction:column;align-items:center;justify-content:center;text-align:center;font-size:7.3px;line-height:8.7px;color:#2b2d33;gap:4px;padding:0 6px}
  .cell.tint{background:var(--tint)}
  .cell.feature{background:var(--brand-blue);color:var(--white);font-size:4.4px;line-height:7.4px;text-align:left;align-items:flex-start;padding:0 7px}
  .cell svg{width:26px;height:26px}
  .solo{left:556px;top:850px;width:104px}

  /* why */
  .why-kicker{left:0;width:1220px;top:974px;text-align:center;font-weight:600}
  .why-title{left:0;width:1220px;top:989px;text-align:center;font-size:12.5px;font-weight:500}
  .why-sub{left:505px;width:210px;top:1008px;text-align:center;font-size:4.3px;line-height:7.5px;color:var(--body)}
  .card{position:absolute;top:1056px;width:78px;height:113px;background:var(--white);box-shadow:0 0 6px rgba(20,30,60,.08);border-radius:3px;padding:0 8px}
  .card.first{box-shadow:none;border-bottom:1px solid var(--brand-blue);border-radius:0 0 4px 4px}
  .card svg.ic{position:absolute;left:7px;top:17px;width:24px;height:24px}
  .card h3{position:absolute;left:8px;top:46px;font-size:5px;font-weight:600}
  .card p{position:absolute;left:8px;top:60px;width:60px;font-size:4.4px;line-height:7.6px;color:var(--body)}
  .card .arrow{position:absolute;left:62px;top:96px}
</style>
</head>
<body>

<header>
  <div class="abs brand"><span class="brand-dot"></span>Brimquarta</div>
  <nav class="abs nav"><a class="active" href="#">HOME</a><a href="#">ABOUT US</a><a href="#">SERVICES</a><a href="#">CONTACT US</a></nav>
  <svg class="abs search" width="9" height="9" viewBox="0 0 10 10"><circle cx="4" cy="4" r="3" fill="none" stroke="#222" stroke-width="0.9"/><line x1="6.2" y1="6.2" x2="9" y2="9" stroke="#222" stroke-width="0.9"/></svg>
  <div class="abs call-btn"><span>+1</span><span>5550148224</span></div>
</header>

<section>
  <div class="abs hero-photo" role="img" aria-label="Businessman in a dark suit holding a tablet with glowing digital network graphics"></div>
  <p class="abs hero-kicker">Transforming the Way You Do Business</p>
  <h1 class="abs hero-title">EVERY BUSINESS<br>IS <b>UNIQUE</b></h1>
  <p class="abs hero-copy">That's why we take a personalized approach to every project, working closely with you to understand your goals and create tailored solutions that work for you.</p>
  <a class="abs hero-btn">Know more</a>
</section>

<section>
  <p class="abs kicker about-kicker">Innovative Solutions</p>
  <h2 class="abs about-title">We believe in pushing the boundaries of what is possible.</h2>
  <p class="abs about-copy">Our team of experts are dedicated to crafting innovative solutions that help your business thrive. From cutting-edge AI and analytics to customer loyalty and digital transformation, we provide what you need to succeed in today's fast-paced business world.</p>
  <div class="abs about-btn">ABOUT US IN DETAIL</div>
  <div class="abs photo-back" role="img" aria-label="Professional reviewing glowing data charts on a transparent screen"></div>
  <div class="abs photo-front" role="img" aria-label="Hand touching an AI chip interface surrounded by technology icons"></div>
</section>

<svg class="tri" width="1200" height="1200" aria-hidden="true">
  <polygon points="410,417 506,495 410,579" fill="var(--tri)"/>
  <polygon points="806,898 709,979 806,1061" fill="var(--tri)"/>
</svg>

<section>
  <p class="abs kicker focus-kicker">Think - Create - Solve</p>
  <h2 class="abs focus-title">Area of focus</h2>
  <p class="abs focus-sub">Helping businesses of all sizes reach their full potential.</p>

  <div class="abs grid">
    <div class="cell">
      <svg viewBox="0 0 26 26" fill="none" stroke="#222" stroke-width="0.8"><rect x="4" y="2" width="14" height="22"/><line x1="6" y1="5" x2="14" y2="5"/><line x1="6" y1="7" x2="12" y2="7"/><circle cx="10" cy="14" r="3.5"/><path d="M10 10.5V14h3.5"/><path d="M6 22l3-3 2 2 4-4"/><path d="M18 8l4-4 1 1-4 4z"/></svg>
      <span>Strategy, Value Creation &amp; Interim CxO</span>
    </div>
    <div class="cell tint">
      <svg viewBox="0 0 26 26" fill="none" stroke="#222" stroke-width="0.8"><rect x="3" y="8" width="14" height="15"/><rect x="12" y="2" width="11" height="6" rx="1"/><circle cx="8" cy="15" r="3"/><line x1="6" y1="13" x2="10" y2="17"/><rect x="13" y="11" width="8" height="3"/><rect x="13" y="15" width="8" height="3"/><rect x="13" y="19" width="8" height="3"/></svg>
      <span>CRM and loyalty solutions</span>
    </div>
    <div class="cell">
      <svg viewBox="0 0 26 26" fill="none" stroke="#222" stroke-width="0.8"><rect x="3" y="3" width="6" height="6"/><rect x="17" y="3" width="6" height="6"/><rect x="3" y="17" width="6" height="6"/><rect x="17" y="17" width="6" height="6"/><circle cx="13" cy="13" r="2.5"/><path d="M16 6h-5M10 20h5M6 10v5M20 16v-5"/></svg>
      <span>M&amp;A -Integration Carve-outs, IMO &amp; TSAs</span>
    </div>

    <div class="cell tint">
      <svg viewBox="0 0 26 26" fill="none" stroke="#222" stroke-width="0.8"><circle cx="8" cy="7" r="4"/><circle cx="8" cy="7" r="1.8"/><circle cx="18" cy="15" r="2.5"/><path d="M14 25v-4a4 4 0 0 1 8 0v4"/><path d="M14 6h4v4"/><path d="M10 19H5v-4"/></svg>
      <span>Change management &amp; Org Design</span>
    </div>
    <div class="cell">
      <svg viewBox="0 0 26 26" fill="none" stroke="#222" stroke-width="0.8"><circle cx="13" cy="9" r="4"/><path d="M11 24v-8a2 2 0 0 1 4 0v3l4 1v4"/><circle cx="3" cy="5" r="1.2"/><circle cx="23" cy="5" r="1.2"/><circle cx="3" cy="13" r="1.2"/><circle cx="23" cy="13" r="1.2"/><path d="M4 5h5M17 5h5M4 13h5M17 13h5"/></svg>
      <span>Digital transformation &amp; Application Development</span>
    </div>
    <div class="cell tint">
      <svg viewBox="0 0 26 26" fill="none" stroke="#222" stroke-width="0.8"><path d="M9 10V7a4 4 0 0 1 8 0v3"/><rect x="7" y="10" width="12" height="11" rx="2"/><circle cx="13" cy="15" r="1.5"/><path d="M2 12h5M2 16h5M19 12h5M19 16h5M13 21v3"/></svg>
      <span>AI, Analytics &amp; Security</span>
    </div>

    <div class="cell">
      <svg viewBox="0 0 26 26" fill="none" stroke="#222" stroke-width="0.8"><circle cx="13" cy="16" r="8"/><circle cx="13" cy="14" r="2.5"/><path d="M8.5 21a5 5 0 0 1 9 0"/><path d="M13 2l1 2 2 .3-1.5 1.4.4 2-1.9-1-1.9 1 .4-2L10 4.3l2-.3z"/><path d="M6 5l.8 1.6 1.7.2-1.2 1.2.3 1.7L6 8.9 4.4 9.7l.3-1.7L3.5 6.8l1.7-.2z"/><path d="M20 5l.8 1.6 1.7.2-1.2 1.2.3 1.7-1.6-.8-1.6.8.3-1.7-1.2-1.2 1.7-.2z"/></svg>
      <span>Customer experience</span>
    </div>
    <div class="cell feature">It is a long established fact that a reader will be distracted by the readable content of a page when looking at its layout. The point of using Lorem Ipsum is that it has a more-or-less normal distribution of letters, as opposed to using 'Content here.</div>
    <div class="cell">
      <svg viewBox="0 0 26 26" fill="none" stroke="#222" stroke-width="0.8"><circle cx="13" cy="13" r="8"/><circle cx="13" cy="13" r="5"/><text x="13" y="14.6" font-size="4.2" text-anchor="middle" fill="#222" stroke="none" font-family="Poppins,sans-serif">ERP</text><path d="M13 2v3M13 21v3M2 13h3M21 13h3M5 5l2 2M19 19l2 2M21 5l-2 2M5 21l2-2"/></svg>
      <span>Complex global ERP &amp; Compliance</span>
    </div>
  </div>

  <div class="abs cell solo">
    <svg viewBox="0 0 26 26" fill="none" stroke="#222" stroke-width="0.8"><circle cx="6" cy="4" r="2"/><path d="M3 10a3 3 0 0 1 6 0"/><circle cx="20" cy="6" r="3"/><circle cx="13" cy="13" r="3"/><path d="M11.7 13l1 1 2-2"/><rect x="3" y="17" width="6" height="7"/><rect x="17" y="17" width="5" height="7"/><path d="M10 6h6M20 10v2M16 20h-6"/></svg>
    <span>Shared service PMO &amp; Automation</span>
  </div>
</section>

<section>
  <p class="abs kicker why-kicker">Why Choose us?</p>
  <h2 class="abs why-title">what makes us different</h2>
  <p class="abs why-sub">Our differences lie in the unique blend of experiences, perspectives, and individual qualities of our Business!</p>

  <div class="card first" style="left:439px">
    <svg class="ic" viewBox="0 0 24 24" fill="none" stroke="var(--brand-blue)" stroke-width="0.8"><circle cx="12" cy="12" r="11"/><circle cx="12" cy="12" r="6"/><circle cx="12" cy="12" r="2.5"/><path d="M12 12l6-6M16 6h2v2"/></svg>
    <h3>Vision</h3><p>Lorem Ipsum is simply dummy text</p>
    <svg class="arrow" width="8" height="4" viewBox="0 0 8 4"><path d="M0 2h7M5.5 .6L7 2 5.5 3.4" fill="none" stroke="var(--brand-blue)" stroke-width="0.5"/></svg>
  </div>
  <div class="card" style="left:526px">
    <svg class="ic" viewBox="0 0 24 24" fill="none" stroke="var(--brand-blue)" stroke-width="0.8"><circle cx="12" cy="12" r="11"/><path d="M9 13a4 4 0 1 1 6 0v2H9z"/><path d="M10 17h4M12 4V5M6 7l1 1M18 7l-1 1"/></svg>
    <h3>strategy</h3><p>Lorem Ipsum is simply dummy text</p>
  </div>
  <div class="card" style="left:613px">
    <svg class="ic" viewBox="0 0 24 24" fill="none" stroke="var(--brand-blue)" stroke-width="0.8"><circle cx="12" cy="12" r="11"/><rect x="6" y="8" width="11" height="9"/><path d="M8 15l3-3 2 2 3-3M14 5l4 4"/></svg>
    <h3>Planning</h3><p>Lorem Ipsum is simply dummy text</p>
  </div>
  <div class="card" style="left:700px">
    <svg class="ic" viewBox="0 0 24 24" fill="none" stroke="var(--brand-blue)" stroke-width="0.8"><circle cx="12" cy="12" r="11"/><rect x="6" y="6" width="4" height="4"/><circle cx="15" cy="12" r="3"/><circle cx="15" cy="12" r="1"/><rect x="6" y="14" width="4" height="4"/><path d="M8 10v4"/></svg>
    <h3>Process</h3><p>Lorem Ipsum is simply dummy text</p>
  </div>
</section>

</body>
</html>
```